Business Card Design

It's an investment advisory service for individuals with all there investment needs. Also financial consulting to businesses and governmental agencies on retirement plans etc. It's personalized not commoditized help. Should show strength, knowledge and money orientation.
Updates

Reason: Will be out of town setting up office.

Reason: waiting for the 2/3rds of group to vote

Reason: only half the votes are in, I'm calling and getting verbals, but at this time we are down to 2 designs.

Industry/Entity Type

Investment

Contact Information for Business Card

B. Rel K. Financial Consulting and Wealth Management, Desmond Wick Harlow, 5172 Paseo Loma Verde Crest, San Diego, CA 92131-4817, Registered Investment Advisor

Requirements
Nice to have
• Something money oriented

```html
<!DOCTYPE html>
<html lang="en">
<head>
<meta charset="utf-8">
<title>B. Rel K. Financial Consulting and Wealth Management – Business Card</title>
<link rel="stylesheet" href="https://fonts.googleapis.com/css2?family=Roboto+Condensed:wght@800&family=PT+Sans:wght@400;700&display=swap">
<style>
  :root {
    --page-bg: #e9e9e9;
    --card-lime: #a9cc2b;
    --card-lime-deep: #8fb51f;
    --band-orange: #f0b125;
    --brand-blue: #1a8fd6;
    --ink-dark: #1d1d1b;
    --ink-muted: #3c4a1a;
    --divider: #ffffff;
  }
  * { margin: 0; padding: 0; box-sizing: border-box; }
  html, body {
    width: 1200px; height: 1200px; overflow: hidden;
    background: var(--page-bg);
  }
  .stage {
    width: 1200px; height: 1200px;
    display: flex; align-items: center; justify-content: center;
  }
  .business-card {
    position: relative;
    width: 1000px; height: 571px;
    background: var(--card-lime);
    overflow: hidden;
    box-shadow: 0 18px 40px rgba(0,0,0,0.18);
    font-family: "PT Sans", Arial, sans-serif;
  }
  .money-visual {
    position: absolute; right: 0; bottom: 0;
    width: 520px; height: 300px;
    background: radial-gradient(ellipse at 60% 70%, rgba(196,214,90,0.85) 0%, rgba(160,190,50,0.6) 45%, rgba(169,204,43,0) 80%);
  }
  .brand-lockup {
    position: absolute; left: 90px; top: 62px;
    display: flex; align-items: flex-end; gap: 22px;
  }
  .brand-mark {
    display: flex; align-items: center; gap: 12px;
    font-family: "Roboto Condensed", "Arial Narrow", sans-serif;
    font-weight: 800; font-size: 64px; line-height: 1;
    color: var(--brand-blue);
  }
  .brand-mark .brand-square {
    width: 34px; height: 34px; background: var(--brand-blue);
  }
  .company-name {
    font-family: "Roboto Condensed", "Arial Narrow", sans-serif;
    font-weight: 800; font-size: 34px; line-height: 1.05;
    color: var(--ink-dark);
    margin-bottom: -70px;
  }
  .name-band {
    position: absolute; left: 0; top: 215px;
    width: 100%; height: 52px;
    background: var(--band-orange);
  }
  .advisor-name {
    position: absolute; left: 60px; top: 222px;
    font-weight: 700; font-size: 31px;
    color: var(--ink-muted);
  }
  .advisor-role {
    position: absolute; left: 560px; top: 232px;
    padding-left: 14px;
    border-left: 2px solid var(--divider);
    font-size: 22px; color: var(--ink-dark);
  }
  .address {
    position: absolute; left: 60px; top: 285px;
    font-size: 25px; line-height: 1.25;
    color: var(--ink-muted);
  }
  .contact-list {
    position: absolute; left: 540px; top: 292px;
    list-style: none;
    font-size: 23px; line-height: 1.5;
    color: var(--ink-dark);
  }
  .contact-list li { display: flex; align-items: center; gap: 12px; }
  .contact-list svg { width: 20px; height: 20px; flex: none; }
</style>
</head>
<body>
<main class="stage">
  <article class="business-card">
    <div class="money-visual" role="img" aria-label="Faded photo of stacked coins with young plants growing from them"></div>

    <div class="brand-lockup">
      <div class="brand-mark"><span class="brand-square"></span>B. Rel K.</div>
      <div class="company-name">Financial Consulting and<br>Wealth Management</div>
    </div>

    <div class="name-band"></div>
    <div class="advisor-name">Desmond Wick Harlow</div>
    <div class="advisor-role">Registered Investment Advisor</div>

    <address class="address" style="font-style:normal">
      5172 Paseo Loma Verde Crest,<br>San Diego, CA 92131-4817
    </address>

    <ul class="contact-list">
      <li>
        <svg viewBox="0 0 20 20" aria-hidden="true"><rect x="1" y="3" width="18" height="14" rx="2" fill="#8a3a1a"/><rect x="5" y="6" width="10" height="5" fill="#f0b125"/></svg>
        (xxx) xxx-xxxx
      </li>
      <li>
        <svg viewBox="0 0 20 20" aria-hidden="true"><rect x="5" y="1" width="10" height="18" rx="2" fill="#8a3a1a"/><rect x="7" y="4" width="6" height="9" fill="#f0b125"/></svg>
        xxxxxxxxxx
      </li>
      <li>
        <svg viewBox="0 0 20 20" aria-hidden="true"><rect x="1" y="4" width="18" height="12" rx="1" fill="#8a3a1a"/><path d="M1 5 L10 11 L19 5" stroke="#f0b125" stroke-width="1.5" fill="none"/></svg>
        xxxxxx@xxxxxxxx.com
      </li>
    </ul>
  </article>
</main>
</body>
</html>
```